business card/stationary for dental office
Bright Harbor Dental Care
business card/stationary for dental office - Health
Creative Brief
Professional
R. Warren Halvik, DDS
Team Leader
2847 NW 42nd Ave Del City, OK 73115
info@brightharbordentalcare.example
brightharbordentalcare.example
I'll attach and example picture of what i want. text "NO INSURANCE, NO PROBLEM!". "Ask us about our Chairside Savings Plan."
quillmoth quillmoth
pbrandle pbrandle
definately want the back silver not blue

```html
<!DOCTYPE html>
<html lang="en">
<head>
<meta charset="utf-8">
<title>Bright Harbor Dental Care – Business Card</title>
<link rel="stylesheet" href="https://fonts.googleapis.com/css2?family=Open+Sans:ital,wght@0,400;0,600;0,700;0,800;1,400&display=swap">
<style>
  :root {
    --backdrop: #d9dadb;
    --card: #ffffff;
    --brand-blue: #1f7fd4;
    --ink: #2e2e2e;
    --ink-soft: #555a60;
    --silver-light: #f1f2f3;
    --silver-mid: #d3d6d9;
    --silver-dark: #a9adb2;
  }
  * { box-sizing: border-box; margin: 0; padding: 0; }
  html, body {
    width: 1200px; height: 878px; overflow: hidden;
    background: var(--backdrop);
    font-family: "Open Sans", Arial, sans-serif;
    color: var(--ink);
  }
  .card {
    position: absolute;
    width: 560px; height: 320px;
    background: var(--card);
    box-shadow: 0 6px 18px rgba(0,0,0,0.18);
    overflow: hidden;
  }
  .card--back {
    left: 610px; top: 120px;
    background: linear-gradient(135deg, var(--silver-light) 0%, var(--silver-mid) 55%, var(--silver-dark) 100%);
    text-align: center;
  }
  .card--front { left: 30px; top: 420px; }

  .brand {
    display: flex; align-items: center; gap: 10px;
    color: var(--brand-blue);
    font-weight: 600;
    font-size: 22px;
    letter-spacing: 0.5px;
    line-height: 1.1;
  }
  .brand__dot {
    width: 34px; height: 34px; border-radius: 50%;
    background: var(--silver-dark);
    flex: none;
  }
  .card--back .brand { position: absolute; left: 0; right: 0; top: 96px; justify-content: center; }
  .card--back .brand__dot { background: #ffffff; }
  .card--front .brand { position: absolute; left: 30px; top: 44px; font-size: 19px; }

  .offer { position: absolute; left: 0; right: 0; top: 168px; }
  .offer__headline {
    font-weight: 800; font-size: 20px; letter-spacing: 1px; color: var(--ink);
  }
  .offer__note {
    font-size: 13px; color: var(--ink-soft); margin-top: 8px;
  }

  .holder { position: absolute; left: 300px; top: 118px; }
  .holder__name { font-weight: 700; font-size: 15px; color: var(--ink); }
  .holder__role { font-style: italic; font-size: 11.5px; color: var(--brand-blue); margin-top: 2px; }
  .holder__address { font-size: 11px; color: var(--ink-soft); margin-top: 8px; line-height: 1.35; }

  .contacts { position: absolute; left: 300px; top: 204px; list-style: none; }
  .contacts li {
    display: flex; align-items: center; gap: 7px;
    font-size: 11px; color: var(--ink-soft); line-height: 16px;
  }
  .contacts svg { width: 9px; height: 9px; fill: var(--brand-blue); flex: none; }

  .footer-bands { position: absolute; left: 0; bottom: 0; width: 560px; height: 64px; }
  .website {
    position: absolute; left: 165px; bottom: 11px;
    font-size: 12px; color: #ffffff; letter-spacing: 0.3px;
  }
</style>
</head>
<body>
  <section class="card card--back" aria-label="Card back">
    <div class="brand"><span class="brand__dot"></span>Bright Harbor Dental Care</div>
    <div class="offer">
      <p class="offer__headline">NO INSURANCE, NO PROBLEM!</p>
      <p class="offer__note">Ask us about our Chairside Savings Plan.</p>
    </div>
  </section>

  <section class="card card--front" aria-label="Card front">
    <div class="brand"><span class="brand__dot"></span>Bright Harbor Dental Care</div>

    <div class="holder">
      <p class="holder__name">R. Warren Halvik, DDS</p>
      <p class="holder__role">Team Leader</p>
      <p class="holder__address">2847 NW 42nd Ave<br>Del City, OK 73115</p>
    </div>

    <ul class="contacts">
      <li><svg viewBox="0 0 10 10"><path d="M2 0h2l1 3-1.5 1a6 6 0 0 0 2.5 2.5L7 5l3 1v2a2 2 0 0 1-2 2A8 8 0 0 1 0 2a2 2 0 0 1 2-2z"/></svg>405 555 0148</li>
      <li><svg viewBox="0 0 10 10"><rect x="0" y="3" width="10" height="5"/><rect x="2" y="0" width="6" height="3"/></svg>405 555 0149</li>
      <li><svg viewBox="0 0 10 10"><path d="M0 2h10v6H0z M0 2l5 3.5L10 2"/></svg>info@brightharbordentalcare.example</li>
    </ul>

    <svg class="footer-bands" viewBox="0 0 560 64" aria-hidden="true">
      <defs>
        <linearGradient id="silver" x1="0" y1="0" x2="1" y2="1">
          <stop offset="0" stop-color="#e4e6e8"/>
          <stop offset="1" stop-color="#a9adb2"/>
        </linearGradient>
      </defs>
      <polygon points="0,8 175,8 155,64 0,64" fill="url(#silver)"/>
      <polygon points="150,26 560,26 560,64 136,64" fill="#1f7fd4"/>
    </svg>
    <p class="website">www.brightharbordentalcare.example</p>
  </section>
</body>
</html>
```